Business Cards for Marco and Tobin

Design of business cards for two people with the recently created brand Valcor Mobile. Valcor Mobile wants to become a worldwide major player on the secondhand phone market. It gathers send hand phones from individuals, refurbish them and sell them throughout the world. It has a green impact (recycling) and we also contribute to social project in Africa (a percentage of our benefits are sent to build school, sport facilities, etc.

Target Market(s)

B2B - Marco and Tobin are in contact with distributors across Africa.

Industry/Entity Type

Wireless Communication

Contact Information for Business Card

Marco Feuillet
Head of Emerging Markets
Valcor Energy South Africa (Pty) Ltd
Kestrel Road 47
2031 Sandton - Johannesburg
South Africa
Tel: + 27 10 555 0148
Mobile : +27 82 55 104
Email : marco.feuillet@valcormobile.example
Skype: marco.feuillet
Web: www.valcormobile.example
 

Tobin Farrow
Head of Southern Africa
Kestrel Road 47
South Africa
Tel: + 27 10 555 0148
Mobile: +27 83 555 0276
Email: tobin.farrow@valcormobile.example
Skype: tobin.farrow
Web: www.valcormobile.example

Requirements
Must have
• The cards need to be "serious", trustable, with a worldwide presence.
Nice to have
• Some "green" / recycling touch would be nice but not necessary if in contradiction with the general design.

```html
<!DOCTYPE html>
<html lang="en">
<head>
<meta charset="utf-8">
<title>Valcor Mobile – Business Card, Marco Feuillet</title>
<link rel="stylesheet" href="https://fonts.googleapis.com/css2?family=Open+Sans:wght@400;600;700&display=swap">
<style>
  :root {
    --backdrop: #1f2023;
    --card: #3b3d41;
    --card-edge: #55585d;
    --brand-blue: #2e8ec6;
    --band-text: #14324a;
    --silver: #d9dcdf;
    --ink-light: #c9ccd0;
    --icon: #b8bcc1;
  }
  * { box-sizing: border-box; margin: 0; padding: 0; }
  html, body {
    width: 1200px; height: 1200px; overflow: hidden;
    background: var(--backdrop);
    font-family: "Open Sans", Arial, sans-serif;
  }
  .stage {
    width: 1200px; height: 1200px;
    display: flex; align-items: center; justify-content: center;
  }
  .business-card {
    position: relative;
    width: 1000px; height: 572px;
    background: var(--card);
    border: 1px solid var(--card-edge);
    border-radius: 0 0 36px 0;
    overflow: hidden;
  }
  .brand {
    position: absolute; left: 70px; top: 300px;
    display: flex; align-items: center; gap: 22px;
  }
  .brand-mark {
    width: 64px; height: 64px;
    background: var(--brand-blue);
    border-radius: 10px;
  }
  .brand-name {
    font-weight: 700; font-size: 84px; letter-spacing: -2px;
    color: var(--silver); line-height: 1;
  }
  .contact {
    position: absolute; left: 620px; top: 62px;
    color: var(--ink-light);
  }
  .contact-name {
    font-size: 32px; font-weight: 400; letter-spacing: 1px;
    text-transform: uppercase; line-height: 1.1;
  }
  .contact-title { font-size: 21px; margin-bottom: 22px; }
  .contact-list { list-style: none; font-size: 19px; line-height: 1.6; }
  .contact-list li { display: flex; align-items: center; gap: 12px; }
  .contact-list .gap { margin-top: 14px; }
  .contact-list svg { width: 18px; height: 18px; flex: none; }
  .address-band {
    position: absolute; left: 0; right: 0; bottom: 0;
    height: 132px;
    background: var(--brand-blue);
    padding: 26px 70px;
    color: var(--band-text);
    font-size: 22px; line-height: 1.45;
  }
</style>
</head>
<body>
<main class="stage">
  <article class="business-card">
    <div class="brand">
      <span class="brand-mark" aria-hidden="true"></span>
      <span class="brand-name">Valcor Mobile</span>
    </div>

    <section class="contact">
      <h1 class="contact-name">Marco Feuillet</h1>
      <p class="contact-title">Head of Emerging Markets</p>
      <ul class="contact-list">
        <li>
          <svg viewBox="0 0 18 18" aria-hidden="true"><rect x="5" y="1" width="8" height="16" rx="1.5" fill="none" stroke="var(--icon)" stroke-width="1.6"/><line x1="8" y1="14" x2="10" y2="14" stroke="var(--icon)" stroke-width="1.6"/></svg>
          +27 82 55 104
        </li>
        <li>
          <svg viewBox="0 0 18 18" aria-hidden="true"><path d="M4 2 L7 2 L8 6 L6 7.5 C7 10 8 11 10.5 12 L12 10 L16 11 L16 14 C16 15 15 16 14 16 C8 16 2 10 2 4 C2 3 3 2 4 2 Z" fill="var(--icon)"/></svg>
          + 27 10 555 0148
        </li>
        <li class="gap">
          <svg viewBox="0 0 18 18" aria-hidden="true"><rect x="1" y="1" width="16" height="16" rx="3" fill="var(--brand-blue)"/></svg>
          marco.feuillet
        </li>
        <li>
          <svg viewBox="0 0 18 18" aria-hidden="true"><g fill="none" stroke="var(--icon)" stroke-width="1.4"><circle cx="9" cy="9" r="7.5"/><ellipse cx="9" cy="9" rx="3.2" ry="7.5"/><line x1="1.5" y1="9" x2="16.5" y2="9"/></g></svg>
          www.valcormobile.example
        </li>
        <li>
          <svg viewBox="0 0 18 18" aria-hidden="true"><rect x="1" y="4" width="16" height="11" rx="1" fill="var(--icon)"/></svg>
          marco.feuillet@valcormobile.example
        </li>
      </ul>
    </section>

    <footer class="address-band">
      <p>Valcor Energy South Africa (Pty) Ltd</p>
      <p>Kestrel Road 47, 2031 Sandton - Johannesburg, South Africa</p>
    </footer>
  </article>
</main>
</body>
</html>
```